Healing stone/crystal Shopify store

Hi - I'm creating a new site to sell healing crystals/stones.Name for the shop is MoonpetalHaven. Site helps people to choose best crystals for them .Shop should have blog aswell.The site should be informative and attractive. Stones we sell Opalite,Green Aventurine,Watermelon Crystal,Rose Quartz Stone,Tiger Eye Stone. Must be Shopify. No content yet, you can fill neccessary fields Lorea Ipsum and if you have some good idea you can put it there
Updates

Designs look the same

Target Market(s)

Woman, English speaking countries.

Industry/Entity Type

Shop

Number of Pages Required

1 page

Colors

Designer to choose colors to be used in the design.

Requirements
Must have
• Blog
Nice to have
• High quality pictures to look site attractive.

```html
<!DOCTYPE html>
<html lang="en">
<head>
<meta charset="utf-8">
<title>MoonpetalHaven – Products</title>
<link href="https://fonts.googleapis.com/css2?family=Roboto:wght@400;500;700&family=Open+Sans:wght@400;600&display=swap" rel="stylesheet">
<style>
:root{
  --accent:#3bb8ef;
  --ink:#222428;
  --muted:#555;
  --line:#e2e2e2;
  --card-border:#d8d8d8;
  --tile:#f0f0f0;
  --footer:#141729;
  --white:#fff;
}
*{box-sizing:border-box;margin:0;padding:0}
html,body{width:1200px;height:2230px;overflow:hidden;background:var(--white)}
body{position:relative;font-family:"Open Sans",Arial,sans-serif;color:var(--ink)}
.promo-bar{position:absolute;top:0;left:0;width:1200px;height:31px;background:var(--accent);color:var(--white);font:500 14px/31px "Roboto",sans-serif;text-align:center}
.promo-bar .close{position:absolute;right:90px;top:0}
.site-header{position:absolute;top:31px;left:0;width:1200px;height:128px;border-bottom:1px solid var(--line)}
.currency{position:absolute;left:98px;top:60px;font:400 14px "Roboto",sans-serif;display:flex;align-items:center;gap:18px}
.currency .select{border:1px solid #999;width:63px;height:25px;font-size:12px;line-height:23px;padding-left:8px;position:relative}
.currency .select svg{position:absolute;right:6px;top:9px}
.brand{position:absolute;left:0;width:1200px;top:44px;text-align:center;font:700 38px "Roboto",sans-serif;color:var(--ink);letter-spacing:.5px}
.header-search{position:absolute;right:98px;top:62px;font:400 14px "Roboto",sans-serif;display:flex;align-items:center;gap:14px}
.main-nav{position:absolute;top:160px;left:0;width:1200px;height:50px;border-bottom:1px solid var(--line)}
.main-nav a{position:absolute;top:0;height:50px;font:500 16px/50px "Roboto",sans-serif;color:var(--ink);text-decoration:none;text-transform:uppercase}
.main-nav .sep{position:absolute;top:14px;width:1px;height:22px;background:var(--line)}
.main-nav .active{background:var(--accent);color:var(--white);left:271px;width:139px;padding-left:28px}
.main-nav .active svg{position:absolute;right:16px;top:20px}
.cart{position:absolute;right:98px;top:14px;font:400 14px "Roboto",sans-serif;display:flex;align-items:center;gap:12px}
.cart .count{position:absolute;right:-6px;top:-8px;width:15px;height:15px;border-radius:50%;background:var(--accent);color:#fff;font-size:9px;text-align:center;line-height:15px}
.hero{position:absolute;top:210px;left:0;width:1200px;height:281px;background:radial-gradient(ellipse at 90% 95%,#6fb79a 0 5%,transparent 14%),linear-gradient(180deg,#4a5244 0%,#2e3429 45%,#1f1f1a 100%)}
.hero h1{position:absolute;top:170px;width:100%;text-align:center;font:700 50px "Roboto",sans-serif;color:var(--white);transform:translateY(-50%)}
.section-title{position:absolute;top:545px;width:1200px;text-align:center;font:500 35px "Roboto",sans-serif;color:var(--ink)}
.product-grid{position:absolute;top:641px;left:97px;display:grid;grid-template-columns:repeat(4,230px);grid-template-rows:repeat(3,386px);column-gap:28px;row-gap:0}
.product-card{width:230px;text-align:center}
.product-thumb{width:230px;height:242px;border:1px solid var(--card-border);padding:4px}
.product-thumb div{width:100%;height:100%}
.product-name{margin-top:16px;font:400 16px/23px "Roboto",sans-serif;color:var(--ink)}
.product-price{margin-top:8px;font:italic 400 16px "Roboto",sans-serif;color:var(--accent)}
.site-footer{position:absolute;top:1825px;left:0;width:1200px;height:284px;background:var(--footer);color:var(--white)}
.footer-col{position:absolute;top:40px}
.footer-col h3{font:500 20px "Roboto",sans-serif;text-transform:uppercase}
.footer-col ul{list-style:none;margin-top:18px}
.footer-col li{font-size:12.5px;line-height:24px;padding-left:22px;position:relative}
.footer-col li:before{content:"";position:absolute;left:4px;top:9px;border-left:5px solid #fff;border-top:3.5px solid transparent;border-bottom:3.5px solid transparent}
.col-divider{position:absolute;top:40px;width:1px;height:150px;background:#23273a}
.newsletter p{color:var(--accent);font-size:14px;margin-top:18px}
.newsletter form{display:flex;gap:14px;margin-top:16px}
.newsletter .email{width:276px;height:42px;background:#fff;color:#333;font-size:12px;line-height:42px;padding-left:14px}
.newsletter .subscribe{width:122px;height:40px;margin-top:1px;background:var(--accent);font:700 14px/40px "Roboto",sans-serif;text-align:center}
.social{position:absolute;top:198px;left:958px;display:flex;gap:12px}
.social span{width:27px;height:27px;border:1.5px solid #fff;border-radius:50%;display:flex;align-items:center;justify-content:center}
.social span i{width:8px;height:8px;background:#fff;border-radius:50%}
.legal{position:absolute;top:2109px;left:0;width:1200px;height:121px;text-align:center}
.payments{display:flex;justify-content:center;gap:11px;margin-top:30px}
.payments span{width:40px;height:25px;border-radius:3px;border:1px solid #ccc}
.copyright{margin-top:18px;font-size:12px;color:#222}
</style>
</head>
<body>
<div class="promo-bar">FREE SHIPPING USA, EUROPE,CANADA, AUSTRALIA <span class="close">X</span></div>

<header class="site-header">
  <div class="currency">Currency <span class="select">CAD<svg width="7" height="5"><path d="M0 0h7L3.5 5z" fill="#222"/></svg></span></div>
  <div class="brand">MoonpetalHaven</div>
  <div class="header-search">Search
    <svg width="16" height="16" viewBox="0 0 16 16"><circle cx="6.5" cy="6.5" r="4.8" fill="none" stroke="#111" stroke-width="2.4"/><path d="M10 10l4.5 4.5" stroke="#111" stroke-width="2.8" stroke-linecap="round"/></svg>
  </div>
</header>

<nav class="main-nav">
  <a href="#" style="left:98px">Home</a><span class="sep" style="left:170px"></span>
  <a href="#" style="left:195px">About</a>
  <a href="#" class="active">Shop by<svg width="10" height="8"><path d="M1 1l4 4 4-4" stroke="#fff" stroke-width="2" fill="none"/></svg></a>
  <a href="#" style="left:436px">Wholesale</a><span class="sep" style="left:553px"></span>
  <a href="#" style="left:578px">Blog</a><span class="sep" style="left:646px"></span>
  <a href="#" style="left:672px">Contact us</a><span class="sep" style="left:801px"></span>
  <a href="#" style="left:827px">Order tracking</a><span class="sep" style="left:995px"></span>
  <div class="cart">Cart
    <span style="position:relative;display:inline-block">
      <svg width="24" height="20" viewBox="0 0 24 20"><path d="M1 7h22l-3 12H4z" fill="#111"/><path d="M6 7l5-6M18 7l-5-6" stroke="#111" stroke-width="2"/></svg>
      <span class="count">0</span>
    </span>
  </div>
</nav>

<section class="hero" role="img" aria-label="Green aventurine stone resting on dark soil among moss">
  <h1>PRODUCTS</h1>
</section>

<h2 class="section-title">MOONPETAL HAVEN</h2>

<main class="product-grid">
  <article class="product-card"><div class="product-thumb"><div role="img" aria-label="Chakra tree of life wire pendant" style="background:radial-gradient(circle,#d9d2c4 0,#f0f0f0 60%)"></div></div><p class="product-name">Nemo enim ipsam<br>voluptatem quia voluptas sit</p><p class="product-price">$89.95</p></article>
  <article class="product-card"><div class="product-thumb"><div role="img" aria-label="Carved tiger eye elephant" style="background:radial-gradient(circle,#7a4a26 0,#a86c3a 30%,#f0f0f0 55%)"></div></div><p class="product-name">Nemo enim ipsam<br>voluptatem quia voluptas sit</p><p class="product-price">$89.95</p></article>
  <article class="product-card"><div class="product-thumb"><div role="img" aria-label="Gemstone chip tree on crystal cluster base" style="background:radial-gradient(circle,#9a8fb0 0,#c7b98a 28%,#f0f0f0 58%)"></div></div><p class="product-name">Nemo enim ipsam<br>voluptatem quia voluptas sit</p><p class="product-price">$89.95</p></article>
  <article class="product-card"><div class="product-thumb"><div role="img" aria-label="Carved blue sandstone angel" style="background:radial-gradient(ellipse 35% 50%,#1e1f55 0,#2a2c6e 50%,#f0f0f0 100%)"></div></div><p class="product-name">Nemo enim ipsam<br>voluptatem quia voluptas sit</p><p class="product-price">$89.95</p></article>

  <article class="product-card"><div class="product-thumb"><div role="img" aria-label="Circle of carved amethyst angels" style="background:radial-gradient(circle,#f0f0f0 0 12%,#5b3f66 25%,#8a6f93 40%,#f0f0f0 60%)"></div></div><p class="product-name">Nemo enim ipsam<br>voluptatem quia voluptas sit</p><p class="product-price">$89.95</p></article>
  <article class="product-card"><div class="product-thumb"><div role="img" aria-label="Red stone tree of life pendant" style="background:radial-gradient(circle,#b3252a 0,#c8434a 30%,#f0f0f0 55%)"></div></div><p class="product-name">Nemo enim ipsam<br>voluptatem quia voluptas sit</p><p class="product-price">$89.95</p></article>
  <article class="product-card"><div class="product-thumb"><div role="img" aria-label="Three carved tiger eye angels" style="background:radial-gradient(ellipse 50% 30%,#7a4c24 0,#a57443 45%,#f0f0f0 100%)"></div></div><p class="product-name">Nemo enim ipsam<br>voluptatem quia voluptas sit</p><p class="product-price">$89.95</p></article>
  <article class="product-card"><div class="product-thumb"><div role="img" aria-label="Gemstone chip tree on rainbow cluster base" style="background:radial-gradient(circle,#d99a3e 0,#a66fb0 30%,#f0f0f0 58%)"></div></div><p class="product-name">Nemo enim ipsam<br>voluptatem quia voluptas sit</p><p class="product-price">$89.95</p></article>

  <article class="product-card"><div class="product-thumb"><div role="img" aria-label="Carved opalite angel" style="background:radial-gradient(ellipse 35% 50%,#e8e0b8 0,#c9d6dc 50%,#f0f0f0 100%)"></div></div><p class="product-name">Nemo enim ipsam<br>voluptatem quia voluptas sit</p><p class="product-price">$89.95</p></article>
  <article class="product-card"><div class="product-thumb"><div role="img" aria-label="Copper wire chakra tree of life pendant" style="background:radial-gradient(circle,#a3552f 0,#8a6aa0 30%,#f0f0f0 58%)"></div></div><p class="product-name">Nemo enim ipsam<br>voluptatem quia voluptas sit</p><p class="product-price">$89.95</p></article>
  <article class="product-card"><div class="product-thumb"><div role="img" aria-label="Ring of assorted carved crystal angels on black" style="background:radial-gradient(circle,#111 0 22%,#c9a3b3 35%,#9b7a52 55%,#1a1a1a 80%)"></div></div><p class="product-name">Nemo enim ipsam<br>voluptatem quia voluptas sit</p><p class="product-price">$89.95</p></article>
  <article class="product-card"><div class="product-thumb"><div role="img" aria-label="Blue stone tree of life pendant" style="background:radial-gradient(circle,#2c4b8e 0,#5a78b5 32%,#f0f0f0 58%)"></div></div><p class="product-name">Nemo enim ipsam<br>voluptatem quia voluptas sit</p><p class="product-price">$89.95</p></article>
</main>

<footer class="site-footer">
  <div class="footer-col" style="left:98px">
    <h3>Quick Links</h3>
    <ul><li>About us</li><li>Contact Us</li><li>Shipping &amp; Handling</li><li>Refunds &amp; Returns</li><li>Moonpetal Haven</li></ul>
  </div>
  <span class="col-divider" style="left:310px"></span>
  <div class="footer-col" style="left:390px">
    <h3>Categories</h3>
    <ul><li>Opalite</li><li>Green Aventurine</li><li>Watermelon Crystal</li><li>Rose Quartz Stone</li><li>Tiger Eye Stone</li></ul>
  </div>
  <span class="col-divider" style="left:626px"></span>
  <div class="footer-col newsletter" style="left:689px">
    <h3>Sign up for newsletter</h3>
    <p>Sign up to our mailing list</p>
    <form><div class="email">Enter email</div><div class="subscribe">SUBSCRIPTION</div></form>
  </div>
  <div class="social"><span><i></i></span><span><i></i></span><span><i></i></span><span><i></i></span></div>
</footer>

<div class="legal">
  <div class="payments">
    <span style="background:#f4f4f4"></span>
    <span style="background:#1b2f6b"></span>
    <span style="background:#1a3f8c"></span>
    <span style="background:#f7e7c4"></span>
  </div>
  <p class="copyright">© 2018 MoonpetalHaven, All Rights Reserved.</p>
</div>
</body>
</html>
```